Hearth Twisters Grand Opening 2-for-1 Sale Postcard Design

Who we are: Hearth Twisters will come to you. We roll your medical marijuana in the privacy and safety of your home. We roll your medicine for you.

We need a postcard design that meets NPDS RCTZ requirements for our Grand Opening 2-for-1 Sale. Please include some or all of our logo.
Looking for elegant, upscale design. Appeal to luxury buyers with more money than time.
Updates

2-for-1 offer good thru March 31, 2015.Please add a small recycle image to convey the fact that we recycle. Added Tuesday, December 8, 2015

Target Market(s)

Income $50K+, Age 35+, College education, Left politically, No kids or older kids

Industry/Entity Type

Health Service

Requirements
Must have
• Our logo
• Our contact number: (574) 218-3065
• NPDS Postcard/RCTZ comptability layout on back of card.
• 2-for-1 Offer good thru March 31st, 2016.
Nice to have
• 2-3 colors, white text on dark green background
Should not have
• Images of marijuana. Please limit marijuana images to our logo.

```html
<!DOCTYPE html>
<html lang="en">
<head>
<meta charset="utf-8">
<title>Hearth Twisters – Grand Opening Postcard</title>
<link rel="stylesheet" href="https://fonts.googleapis.com/css2?family=Lato:wght@400;700;900&family=Oswald:wght@500;600&family=Roboto+Condensed:wght@400;700&display=swap">
<style>
  :root {
    --green-dark: #1f4d2b;
    --green-brand: #2e6b35;
    --green-light: #5cb847;
    --gray-line: #6d6d6d;
    --gray-soft: #d9d9d9;
    --ink: #2b2b2b;
    --white: #ffffff;
    --canvas: #e6e6e6;
  }
  * { margin: 0; padding: 0; box-sizing: border-box; }
  html, body { width: 806px; height: 1200px; overflow: hidden; }
  body { background: var(--canvas); font-family: "Lato", sans-serif; position: relative; }

  .card { position: absolute; left: 49px; width: 708px; background: var(--white); overflow: hidden; box-shadow: 0 2px 6px rgba(0,0,0,.25); }
  .card--front { top: 34px; height: 549px; }
  .card--back { top: 618px; height: 548px; }

  .brand { position: absolute; text-align: center; }
  .brand__mark { display: block; margin: 0 auto 10px; width: 58px; height: 58px; background: var(--green-light); }
  .brand__name { font-family: "Lato", sans-serif; font-weight: 700; color: var(--green-brand); letter-spacing: -0.5px; white-space: nowrap; }

  /* front */
  .front__brand { left: 40px; top: 22px; width: 260px; }
  .front__brand .brand__name { font-size: 34px; }
  .offer-burst { position: absolute; left: 91px; top: 146px; width: 170px; height: 170px; }
  .offer-burst svg { width: 170px; height: 170px; }
  .offer-burst__text { position: absolute; inset: 0; display: flex; flex-direction: column; align-items: center; justify-content: center; color: var(--ink); line-height: 1; }
  .offer-burst__small { font-size: 24px; }
  .offer-burst__big { font-size: 36px; font-weight: 900; color: var(--white); margin: 2px 0; }
  .offer-burst__sale { font-size: 32px; font-weight: 900; }
  .photo-frame { position: absolute; right: 0; top: 0; width: 370px; height: 320px; }
  .divider { position: absolute; left: 0; top: 316px; width: 430px; height: 5px; background: var(--gray-line); }
  .opening-band { position: absolute; left: 0; top: 326px; width: 708px; height: 165px; }
  .opening-band__title { position: absolute; left: 34px; top: 366px; font-family: "Oswald", sans-serif; font-weight: 600; font-size: 50px; color: var(--white); letter-spacing: 0.5px; line-height: 1; }
  .opening-band__terms { position: absolute; left: 36px; top: 436px; font-family: "Lato", sans-serif; font-size: 15px; color: var(--white); letter-spacing: 0.3px; }
  .booking { position: absolute; left: 488px; top: 362px; color: var(--ink); }
  .booking__label { font-family: "Roboto Condensed", sans-serif; font-weight: 700; font-size: 28px; line-height: 1; }
  .booking__label span { color: var(--green-light); }
  .booking__phone { font-family: "Roboto Condensed", sans-serif; font-weight: 400; font-size: 25px; margin-top: 4px; }
  .booking__dot { position: absolute; left: 424px; top: 392px; width: 34px; height: 34px; border-radius: 50%; background: var(--green-dark); }
  .contact-bar { position: absolute; left: 0; bottom: 0; width: 708px; height: 58px; background: var(--green-light); display: flex; align-items: center; padding: 0 30px; color: var(--white); font-size: 15px; font-weight: 700; gap: 22px; }
  .contact-bar__item { display: flex; align-items: center; gap: 7px; }
  .contact-bar__social { margin-left: auto; display: flex; align-items: center; gap: 6px; font-weight: 400; }
  .social-square { width: 17px; height: 17px; background: var(--white); opacity: .9; border-radius: 2px; }

  /* back */
  .back__panel { position: absolute; left: 0; top: 0; width: 360px; height: 548px; }
  .back__brand { left: 20px; top: 26px; width: 300px; }
  .back__brand .brand__name { font-size: 38px; }
  .tagline { position: absolute; left: 0; top: 179px; width: 345px; height: 76px; display: flex; align-items: center; padding-left: 22px; font-family: "Roboto Condensed", sans-serif; font-weight: 700; font-size: 29px; color: var(--ink); background: var(--white); }
  .mission { position: absolute; left: 0; top: 255px; width: 345px; height: 225px; background: var(--green-dark); color: var(--white); text-align: center; padding-top: 40px; }
  .mission__head { font-family: "Roboto Condensed", sans-serif; font-weight: 700; font-size: 17px; margin-bottom: 26px; }
  .mission__body { font-size: 16px; line-height: 1.3; }
  .back-contact { position: absolute; left: 0; top: 480px; width: 358px; height: 68px; background: linear-gradient(90deg, var(--white), var(--gray-soft)); padding: 8px 28px; font-size: 13px; color: var(--ink); line-height: 1.3; }
  .back-contact__row { display: flex; align-items: center; gap: 6px; }
  .recycle { position: absolute; right: 16px; top: 18px; width: 30px; height: 30px; }
  .stamp-box { position: absolute; left: 611px; top: 32px; width: 62px; height: 83px; border: 1px solid var(--ink); }
  .icon { width: 12px; height: 12px; flex: none; }
</style>
</head>
<body>

<section class="card card--front" aria-label="Postcard front">
  <div class="brand front__brand">
    <span class="brand__mark"></span>
    <span class="brand__name">Hearth Twisters</span>
  </div>

  <div class="offer-burst">
    <svg viewBox="0 0 180 180" aria-hidden="true">
      <polygon fill="#5cb847" points="90,0 101,22 120,5 124,29 147,18 143,42 168,39 156,61 180,66 162,82 180,98 158,106 172,127 147,127 154,151 131,145 128,170 109,157 97,180 90,158 79,180 67,157 49,170 46,145 23,151 30,127 6,127 20,106 0,98 17,82 0,66 24,61 12,39 37,42 33,18 56,29 60,5 79,22"/>
    </svg>
    <div class="offer-burst__text">
      <span class="offer-burst__small">Two for</span>
      <span class="offer-burst__big">ONE</span>
      <span class="offer-burst__sale">sale</span>
    </div>
  </div>

  <svg class="photo-frame" viewBox="0 0 370 320" role="img" aria-label="Photo: hands rolling paper on a light table">
    <defs>
      <linearGradient id="photoTone" x1="0" y1="0" x2="1" y2="1">
        <stop offset="0" stop-color="#e4dccf"/>
        <stop offset=".55" stop-color="#cfc3b2"/>
        <stop offset="1" stop-color="#b9a994"/>
      </linearGradient>
    </defs>
    <path d="M55 0 H370 V320 H36 Q14 320 14 298 Z" fill="#5cb847"/>
    <path d="M70 0 H370 V304 H46 Q28 304 28 288 Z" fill="url(#photoTone)"/>
  </svg>

  <div class="divider"></div>

  <svg class="opening-band" viewBox="0 0 708 165" aria-hidden="true">
    <defs>
      <linearGradient id="silver" x1="0" y1="0" x2="1" y2="0">
        <stop offset="0" stop-color="#cfcfcf"/>
        <stop offset=".5" stop-color="#ffffff"/>
        <stop offset="1" stop-color="#e3e3e3"/>
      </linearGradient>
    </defs>
    <rect width="708" height="165" fill="#1f4d2b"/>
    <polygon points="463,0 708,0 708,165 463,165 385,82" fill="url(#silver)"/>
  </svg>
  <h1 class="opening-band__title">GRAND OPENING</h1>
  <p class="opening-band__terms">2-for-1 offer good thru March 31, 2016</p>
  <span class="booking__dot"></span>
  <div class="booking">
    <div class="booking__label">BOOK <span>TODAY</span></div>
    <div class="booking__phone">574-218-3065</div>
  </div>

  <footer class="contact-bar">
    <span class="contact-bar__item">
      <svg class="icon" viewBox="0 0 12 12" aria-hidden="true"><rect x="0.5" y="2" width="11" height="8" fill="#fff"/><path d="M0.5 2 L6 7 L11.5 2" stroke="#5cb847" fill="none"/></svg>
      appointments@hearthtwisters.com
    </span>
    <span class="contact-bar__item">
      <svg class="icon" viewBox="0 0 12 12" aria-hidden="true"><circle cx="6" cy="6" r="5.5" fill="#fff"/><path d="M0.5 6 H11.5 M6 0.5 V11.5" stroke="#5cb847"/></svg>
      www.hearthtwisters.com
    </span>
    <span class="contact-bar__social">follow us <span class="social-square"></span><span class="social-square"></span></span>
  </footer>
</section>

<section class="card card--back" aria-label="Postcard back">
  <svg class="back__panel" viewBox="0 0 360 548" aria-hidden="true">
    <path d="M0 0 H300 Q352 0 352 60 V548 H0 Z" fill="#5cb847"/>
    <path d="M0 0 H296 Q345 0 345 58 V169 H0 Z" fill="#ffffff"/>
  </svg>

  <div class="brand back__brand">
    <span class="brand__mark"></span>
    <span class="brand__name">Hearth Twisters</span>
  </div>

  <div class="tagline">SO YOU DON'T HAVE TO</div>

  <div class="mission">
    <p class="mission__head">HEARTH TWISTERS WILL COME TO YOU</p>
    <p class="mission__body">We roll your medical marijuana in the<br><strong>privacy</strong> and <strong>safety</strong> of your home.<br>We roll your medicine for you.</p>
  </div>

  <div class="back-contact">
    <div class="back-contact__row">
      <svg class="icon" viewBox="0 0 12 12" aria-hidden="true"><path d="M2 1 L4 1 L5 4 L3.5 5 Q5 8 7 8.5 L8 7 L11 8 L11 10 Q10 11.5 8 11 Q2 9 1 3 Q1 1.5 2 1 Z" fill="#2b2b2b"/></svg>
      574-218-3065
    </div>
    <div class="back-contact__row">
      <svg class="icon" viewBox="0 0 12 12" aria-hidden="true"><rect x="0.5" y="2" width="11" height="8" fill="#2b2b2b"/><path d="M0.5 2 L6 7 L11.5 2" stroke="#fff" fill="none"/></svg>
      appointments@hearthtwisters.com
    </div>
    <div class="back-contact__row">
      <svg class="icon" viewBox="0 0 12 12" aria-hidden="true"><circle cx="6" cy="6" r="5.5" fill="#2b2b2b"/><path d="M0.5 6 H11.5 M6 0.5 V11.5" stroke="#fff"/></svg>
      www.hearthtwisters.com
    </div>
    <svg class="recycle" viewBox="0 0 30 30" role="img" aria-label="Recycled">
      <path d="M15 4 A11 11 0 0 1 26 15" fill="none" stroke="#2e6b35" stroke-width="3"/>
      <polygon points="22,14 30,14 26,20" fill="#2e6b35"/>
      <path d="M26 17 A11 11 0 0 1 6 22" fill="none" stroke="#2e6b35" stroke-width="3"/>
      <polygon points="9,18 4,25 2,18" fill="#2e6b35"/>
      <path d="M4 15 A11 11 0 0 1 12 4.5" fill="none" stroke="#2e6b35" stroke-width="3"/>
      <polygon points="11,1 17,4.5 11,8" fill="#2e6b35"/>
    </svg>
  </div>

  <div class="stamp-box"></div>
</section>

</body>
</html>
```